Design my dad a new business card because his current one sucks!

I need a business card designed for my fathers home maintenance business. His customers are individuals (single moms, old people etc.) as well as the occasional business. As such it needs to be accessible to both target audiences.

The front of the card should be dark grey on yellow with the logo and contain the following information:
- Warren Dobrinski
- 0487 362 914
- info@harbourlinehandyworks.com.au
- 0487 362 914

- ABN: 87 214 630 592
- 'Fully Insured'

The reverse should be yellow on dark grey and will have the web address:
- harbourlinehandyworks.com.au

And a few key services he offers:
GENERAL REPAIRS
PAINTING/TILING/
PAVING &CONCRETING
PRESSURE WASHING
ON-SITE WELDING
DECKING ADDITIONS & REPAIRS
FENCING
FULL BOND CLEANING

This will be first time the logo has been printed so you will need to come up with the best CMYK approximation of the RGB colours to make sure it is a close as possible.

```html
<!DOCTYPE html>
<html lang="en">
<head>
<meta charset="utf-8">
<title>Harbourline Handyworks – Business Card</title>
<link rel="stylesheet" href="https://fonts.googleapis.com/css2?family=Questrial&display=swap">
<style>
  :root {
    --card-yellow: #f3d633;
    --card-grey: #404041;
    --page-white: #ffffff;
  }
  * { box-sizing: border-box; margin: 0; padding: 0; }
  html, body {
    width: 1200px;
    height: 348px;
    overflow: hidden;
    background: var(--page-white);
  }
  body {
    position: relative;
    font-family: "Questrial", sans-serif;
  }
  .card {
    position: absolute;
    top: 0;
    width: 579px;
    height: 348px;
  }
  .card-front {
    left: 0;
    background: var(--card-yellow);
    color: var(--card-grey);
  }
  .card-back {
    left: 621px;
    background: var(--card-grey);
    color: var(--card-yellow);
  }

  /* Front */
  .business-meta {
    position: absolute;
    top: 24px;
    right: 31px;
    text-align: right;
    font-size: 16px;
    line-height: 21px;
  }
  .brand-name {
    position: absolute;
    left: 66px;
    top: 104px;
    width: 450px;
    font-size: 56px;
    line-height: 60px;
    letter-spacing: 1px;
    text-transform: uppercase;
    color: var(--card-grey);
  }
  .brand-name span { display: block; }
  .contact {
    position: absolute;
    right: 31px;
    top: 250px;
    text-align: right;
    font-size: 17px;
    line-height: 27px;
  }
  .contact-name { font-size: 18px; font-weight: 400; -webkit-text-stroke: 0.4px var(--card-grey); }

  /* Back */
  .services {
    position: absolute;
    left: 34px;
    top: 24px;
    list-style: none;
    font-size: 26px;
    line-height: 34.3px;
    text-transform: uppercase;
    letter-spacing: 0.2px;
  }
  .web-band {
    position: absolute;
    left: 0;
    bottom: 0;
    width: 100%;
    height: 47px;
    background: var(--card-yellow);
    color: var(--card-grey);
    font-size: 26px;
    line-height: 47px;
    padding-left: 34px;
    letter-spacing: 0.3px;
  }
</style>
</head>
<body>
  <section class="card card-front" aria-label="Card front">
    <div class="business-meta">
      <p>ABN: 87 214 630 592</p>
      <p>'Fully Insured'</p>
    </div>
    <h1 class="brand-name"><span>Harbourline</span><span>Handyworks</span></h1>
    <div class="contact">
      <p class="contact-name">Warren Dobrinski</p>
      <p class="contact-phone">0487 362 914</p>
      <p class="contact-email">info@harbourlinehandyworks.com.au</p>
    </div>
  </section>

  <section class="card card-back" aria-label="Card back">
    <ul class="services">
      <li>General Repairs</li>
      <li>Painting/Tiling/</li>
      <li>Paving &amp;Concreting</li>
      <li>Pressure Washing</li>
      <li>On-Site Welding</li>
      <li>Decking Additions &amp; Repairs</li>
      <li>Fencing</li>
      <li>Full Bond Cleaning</li>
    </ul>
    <div class="web-band">harbourlinehandyworks.com.au</div>
  </section>
</body>
</html>
```